Every Shelf Neatly Sorted or ESN Organized needs a business card design. ESN Organized is a professi

We need a business card design that is clean, sharp and conveys a sense of organization. I already have a logo.

Reason: I am still providing feedback and need more time.

Target Market(s)

Families (specifically mothers), small business owners, parents, seniors

Industry/Entity Type

Business

Contact Information for Business Card

My website is www.esnsortedhome.example and my Facebook page is http://www.facebook.example/everyshelfneatlysorted. The phone number is 555-418-2706 and I want to be listed as Marla V. Osgood, Owner

Requirements
Must have
• My logo.

```html
<!DOCTYPE html>
<html lang="en">
<head>
<meta charset="utf-8">
<title>ESN Organized — Business Card</title>
<link rel="stylesheet" href="https://fonts.googleapis.com/css2?family=Lato:ital,wght@0,400;0,700;1,400&display=swap">
<style>
  :root {
    --backdrop: #dfe3e6;
    --card: #f4f5f6;
    --card-edge: #c9cdd1;
    --brand-blue: #1b4ea3;
    --ink: #2a2a2a;
    --ink-soft: #3a3a3a;
  }
  * { box-sizing: border-box; margin: 0; padding: 0; }
  html, body {
    width: 1200px;
    height: 970px;
    overflow: hidden;
    background: var(--backdrop);
    font-family: "Lato", sans-serif;
  }
  .business-card {
    position: absolute;
    left: 100px;
    top: 185px;
    width: 1000px;
    height: 600px;
    background: var(--card);
    border: 1px solid var(--card-edge);
  }
  .brand-name {
    position: absolute;
    top: 72px;
    left: 0;
    width: 100%;
    text-align: center;
    font-weight: 400;
    font-size: 60px;
    letter-spacing: 0.06em;
    color: var(--brand-blue);
    line-height: 1;
  }
  .tagline {
    position: absolute;
    top: 160px;
    left: 0;
    width: 100%;
    text-align: center;
    font-style: italic;
    font-size: 24px;
    color: var(--ink-soft);
  }
  .holder-name {
    position: absolute;
    top: 338px;
    right: 56px;
    font-weight: 700;
    font-size: 34px;
    color: var(--brand-blue);
  }
  .divider {
    position: absolute;
    top: 385px;
    left: 68px;
    width: 877px;
    height: 3px;
    background: var(--brand-blue);
  }
  .holder-role {
    position: absolute;
    top: 398px;
    right: 56px;
    font-style: italic;
    font-size: 28px;
    color: var(--ink);
  }
  .contact-list {
    position: absolute;
    top: 412px;
    left: 68px;
    list-style: none;
  }
  .contact-item {
    display: flex;
    align-items: center;
    height: 52px;
    font-size: 25px;
    color: var(--ink);
  }
  .contact-icon {
    width: 36px;
    height: 36px;
    margin-right: 14px;
    flex: none;
  }
  .website {
    position: absolute;
    top: 530px;
    left: 74px;
    font-weight: 700;
    font-size: 22px;
    letter-spacing: 0.36em;
    color: var(--brand-blue);
  }
</style>
</head>
<body>
  <article class="business-card">
    <h1 class="brand-name">ESN Organized</h1>
    <p class="tagline">We sort every shelf in every room, so life stays in order</p>

    <h2 class="holder-name">Marla V. Osgood</h2>
    <div class="divider"></div>
    <p class="holder-role">Owner</p>

    <ul class="contact-list">
      <li class="contact-item">
        <svg class="contact-icon" viewBox="0 0 36 36" aria-hidden="true">
          <circle cx="18" cy="18" r="18" fill="var(--brand-blue)"/>
          <path d="M9 15c0-3 4-5 9-5s9 2 9 5l-3 2-2-3h-8l-2 3z" fill="#fff"/>
          <path d="M12 18h12l2 7H10z" fill="#fff"/>
          <circle cx="18" cy="21.5" r="2" fill="var(--brand-blue)"/>
        </svg>
        <span>555-418-2706</span>
      </li>
      <li class="contact-item">
        <svg class="contact-icon" viewBox="0 0 36 36" aria-hidden="true">
          <circle cx="18" cy="18" r="18" fill="var(--brand-blue)"/>
        </svg>
        <span>pages.example/everyshelfneatlysorted</span>
      </li>
    </ul>

    <p class="website">www.esnsortedhome.example</p>
  </article>
</body>
</html>
```